13 Tavo - new website design project

Our company Tavo Electrical is developing a new lead generation website focused on Electrical, LED Lighting and Solar Power. We need a high converting website.

Example of our current website is www.tavoelectrical.com.au You can take content from this website for this new design. Our colours are red, black and white. For our new website we would like to promote Tavo, Bright Days Ahead. Please listen to the jingle.

The below link is the company jingle that we have developed.
http://www.tunecraftaudio.com.au/tav-tc-v1/

The key for this brief is to generate leads for Electrical, LED Lighting (for commercial) and Solar Power & Storage.

Target Market(s)

Business owners in Melbourne Victoria

Number of Pages Required

4 page

Colors
ec1f27
ffffff

Requirements
Must have
• This page must be clean, be in line with company branding and a high converting lead website.

```html
<!DOCTYPE html>
<html lang="en">
<head>
<meta charset="utf-8">
<title>Tavo Electrical</title>
<link rel="stylesheet" href="https://fonts.googleapis.com/css2?family=Mulish:wght@300;400;600;700;800&display=swap">
<style>
  :root {
    --red: #c4202a;
    --red-bright: #ec1f27;
    --red-deep: #a5161e;
    --ink: #1e1e1e;
    --slate: #343840;
    --charcoal: #232323;
    --footer: #1b1b1b;
    --copy: #262626;
    --grey-text: #777;
    --white: #ffffff;
  }
  * { box-sizing: border-box; margin: 0; padding: 0; }
  html, body { width: 1200px; height: 2639px; overflow: hidden; }
  body { font-family: "Mulish", sans-serif; color: var(--ink); background: var(--white); position: relative; }
  section, header, footer { position: absolute; left: 0; width: 1200px; }

  /* Header */
  .site-header { top: 0; height: 118px; background: var(--white); }
  .top-stripes { position: absolute; top: 0; left: 0; width: 1200px; height: 4px;
    background: repeating-linear-gradient(90deg, var(--red) 0 56px, var(--slate) 56px 112px, #fff 112px 118px); }
  .brand { position: absolute; left: 80px; top: 36px; display: flex; align-items: center; gap: 10px; }
  .brand-dot { width: 30px; height: 30px; border-radius: 50%; background: var(--red); }
  .brand-name { font-size: 40px; font-weight: 800; color: var(--ink); letter-spacing: 1px; }
  .main-nav { position: absolute; top: 48px; left: 403px; display: flex; }
  .main-nav a { font-size: 14px; color: var(--ink); text-decoration: none; height: 27px; line-height: 27px; padding: 0 14px; margin-right: 6px; text-transform: uppercase; }
  .main-nav a.active { background: var(--red); color: var(--white); }

  /* Hero */
  .hero { top: 118px; height: 521px; background: #15110f; overflow: hidden; }
  .hero-photo { position: absolute; inset: 0;
    background:
      radial-gradient(ellipse 60% 40% at 30% 70%, rgba(150,110,70,.35) 0%, rgba(150,110,70,0) 70%),
      radial-gradient(ellipse 55% 35% at 75% 65%, rgba(130,100,75,.3) 0%, rgba(130,100,75,0) 70%),
      linear-gradient(180deg, #121212 0%, #1e1b19 30%, #3a332d 62%, #2a2521 82%, #1a1715 100%); }
  .hero-photo::after { content: ""; position: absolute; inset: 0; background: rgba(0,0,0,.28); }
  .hero-title { position: absolute; top: 200px; width: 100%; text-align: center; color: var(--white); font-size: 34px; font-weight: 700; letter-spacing: 1px; z-index: 1; }
  .hero-sub { position: absolute; top: 246px; width: 100%; text-align: center; color: #e6e6e6; font-size: 17px; letter-spacing: .5px; z-index: 1; }
  .btn { display: inline-flex; align-items: center; justify-content: center; gap: 10px; border-radius: 20px; color: var(--white); font-weight: 700; font-size: 14px; }
  .btn svg { width: 14px; height: 14px; }
  .hero-actions .btn { position: absolute; top: 313px; height: 37px; z-index: 1; }
  .btn-primary { background: var(--red); }
  .btn-dark { background: var(--slate); }
  .hero-dots { position: absolute; top: 474px; left: 575px; display: flex; gap: 9px; z-index: 1; }
  .hero-dots span { width: 10px; height: 10px; border-radius: 50%; background: #fff; }
  .hero-dots span.on { background: var(--red); }

  /* About */
  .about { top: 639px; height: 436px; background: var(--white); }
  .section-title { font-size: 28px; font-weight: 300; text-decoration: underline; text-underline-offset: 5px; text-decoration-thickness: 1px; letter-spacing: 1px; }
  .about .section-title { position: absolute; left: 81px; top: 96px; }
  .about-text { position: absolute; left: 81px; top: 160px; width: 570px; font-size: 13px; line-height: 22px; color: var(--grey-text); }
  .about .btn { position: absolute; left: 81px; top: 283px; width: 135px; height: 34px; font-size: 13px; }
  .hex-grid { position: absolute; right: 0; top: 0; width: 496px; height: 436px; }
  .hex-label { font-family: "Mulish", sans-serif; font-size: 8px; font-weight: 700; fill: #fff; text-anchor: middle; }

  /* Why */
  .why { top: 1075px; height: 496px;
    background: radial-gradient(ellipse at 50% 55%, #1b3346 0%, #0c1620 45%, #060607 100%); }
  .why .section-title { position: absolute; top: 70px; width: 100%; text-align: center; color: var(--white); }
  .accordion { position: absolute; left: 315px; top: 146px; width: 568px; }
  .acc-item { display: flex; height: 38px; background: var(--red); margin-bottom: 8px; color: var(--white); font-size: 17px; }
  .acc-item.open { height: 41px; margin-bottom: 0; }
  .acc-sign { width: 44px; display: flex; align-items: center; justify-content: center; border-right: 1px solid rgba(255,255,255,.25); font-size: 18px; }
  .acc-label { display: flex; align-items: center; padding-left: 19px; }
  .acc-body { background: var(--red-deep); height: 80px; padding: 18px 28px 0 28px; color: #f4e6e6; font-size: 13px; line-height: 20px; margin-bottom: 4px; }

  /* Testimonials */
  .testimonials { top: 1571px; height: 454px; background: var(--white); }
  .testimonials .section-title { position: absolute; top: 50px; width: 100%; text-align: center; }
  .quote-mark { position: absolute; left: 278px; top: 0; font-size: 190px; color: #ececec; font-weight: 800; line-height: 1; }
  .avatar { position: absolute; left: 562px; top: 128px; width: 76px; height: 76px; }
  .user-name { position: absolute; top: 237px; width: 100%; text-align: center; font-size: 13px; font-weight: 700; }
  .quote-text { position: absolute; top: 270px; left: 120px; width: 960px; text-align: center; font-size: 18px; line-height: 23px; color: #333; }
  .quote-dots { position: absolute; top: 380px; left: 572px; display: flex; gap: 2px; }
  .quote-dots span { width: 16px; height: 16px; border-radius: 50%; border: 1px solid #555; }
  .quote-dots span.on { background: var(--red); border-color: var(--red); }

  /* Contact */
  .contact { top: 2025px; height: 405px; background: var(--charcoal); }
  .contact .section-title { position: absolute; top: 36px; width: 100%; text-align: center; color: var(--white); }
  .field { position: absolute; background: var(--white); border-radius: 26px; color: #999; font-size: 17px; padding-left: 27px; }
  .field-name { left: 146px; top: 113px; width: 440px; height: 51px; line-height: 51px; }
  .field-email { left: 616px; top: 113px; width: 431px; height: 51px; line-height: 51px; }
  .field-message { left: 146px; top: 183px; width: 908px; height: 125px; padding-top: 16px; }
  .contact .btn { position: absolute; left: 537px; top: 327px; width: 146px; height: 44px; font-size: 13px; }

  /* Footer */
  .site-footer { top: 2430px; height: 142px; background: var(--footer); color: var(--white); }
  .footer-brand { position: absolute; left: 84px; top: 40px; font-size: 52px; font-weight: 800; color: #3a3a3a; letter-spacing: 1px; }
  .footer-label { font-size: 12px; text-transform: uppercase; color: #ddd; }
  .call { position: absolute; left: 378px; top: 45px; display: flex; gap: 14px; }
  .call svg { width: 32px; height: 32px; margin-top: 8px; }
  .call-number { font-size: 22px; font-weight: 800; color: var(--red-bright); margin-top: 2px; }
  .follow { position: absolute; left: 686px; top: 45px; }
  .social { display: flex; gap: 9px; margin-top: 13px; }
  .social span { width: 38px; height: 38px; border-radius: 50%; border: 2px solid #fff; display: flex; align-items: center; justify-content: center; }
  .social span::after { content: ""; width: 12px; height: 12px; border-radius: 50%; background: #fff; }
  .subscribe { position: absolute; left: 920px; top: 45px; }
  .sub-input { margin-top: 12px; width: 201px; height: 31px; background: #000; color: #bbb; font-size: 11px; line-height: 31px; padding-left: 10px; }
  .copyright { position: absolute; left: 0; top: 2572px; width: 1200px; height: 67px; background: var(--copy); color: #ddd; font-size: 13px; text-align: center; line-height: 67px; }
  .to-top { position: absolute; left: 1076px; top: 2550px; width: 44px; height: 44px; border-radius: 50%; background: var(--red); display: flex; align-items: center; justify-content: center; }
</style>
</head>
<body>

<header class="site-header">
  <div class="top-stripes"></div>
  <div class="brand"><span class="brand-dot"></span><span class="brand-name">Tavo</span></div>
  <nav class="main-nav">
    <a class="active">Home</a><a>Electrical</a><a>LED Lighting</a><a>Solar Power</a><a>Our Work</a><a>Contact Us</a>
  </nav>
</header>

<section class="hero">
  <div class="hero-photo" role="img" aria-label="Night aerial view of a city lit up with lights"></div>
  <h1 class="hero-title">AUSTRALIA’S LARGEST</h1>
  <p class="hero-sub">FULLY INTEGRATED ELECTRICAL &amp; ENERGY SOLUTIONS PROVIDER</p>
  <div class="hero-actions">
    <span class="btn btn-primary" style="left:454px;width:141px;">Read More
      <svg viewBox="0 0 14 14"><path d="M1 7h11M8 3l4 4-4 4" stroke="#fff" stroke-width="2" fill="none"/></svg></span>
    <span class="btn btn-dark" style="left:611px;width:132px;">Our Work
      <svg viewBox="0 0 14 14"><path d="M1 7h11M8 3l4 4-4 4" stroke="#fff" stroke-width="2" fill="none"/></svg></span>
  </div>
  <div class="hero-dots"><span class="on"></span><span></span><span></span></div>
</section>

<section class="about">
  <h2 class="section-title">ABOUT US</h2>
  <p class="about-text">Tavo Electrical was formed to be an expert Electricity Contracting Company providing services to all Residential and Commercial Customers. With over 10 years of experience, Tavo Electrical has developed a highly-experienced team of professionals that ensure all our customer expectations are met.</p>
  <span class="btn btn-primary">More Detail
    <svg viewBox="0 0 14 14"><path d="M1 7h11M8 3l4 4-4 4" stroke="#fff" stroke-width="2" fill="none"/></svg></span>

  <svg class="hex-grid" viewBox="400 363 282 248" preserveAspectRatio="none">
    <defs>
      <path id="hex" d="M-64 0L-32 -55.4L32 -55.4L64 0L32 55.4L-32 55.4Z"/>
    </defs>
    <g stroke="#fff" stroke-width="3">
      <use href="#hex" x="465" y="377" fill="#c4202a"/>
      <use href="#hex" x="465" y="597" fill="#c4202a"/>
      <use href="#hex" x="568" y="321" fill="#343840"/>
      <use href="#hex" x="568" y="652" fill="#343840"/>
      <use href="#hex" x="671" y="377" fill="#343840"/>
      <use href="#hex" x="671" y="487" fill="#c4202a"/>
      <use href="#hex" x="671" y="597" fill="#343840"/>
    </g>
    <g stroke="#c4202a" stroke-width="2.5">
      <use href="#hex" x="465" y="487" fill="#2b3038" role="img" aria-label="Electrician working on a switchboard"/>
      <use href="#hex" x="568" y="431" fill="#3d434c" role="img" aria-label="Commercial LED lighting installation"/>
      <use href="#hex" x="568" y="542" fill="#283548" role="img" aria-label="Solar panels on a rooftop"/>
    </g>
    <text class="hex-label" x="465" y="490">ELECTRICAL</text>
    <text class="hex-label" x="568" y="434">LED LIGHTING</text>
    <text class="hex-label" x="568" y="545">SOLAR POWER</text>
  </svg>
</section>

<section class="why" role="img" aria-label="Abstract glowing electrical energy background">
  <h2 class="section-title">WHY CHOOSE US</h2>
  <div class="accordion">
    <div class="acc-item open"><span class="acc-sign">-</span><span class="acc-label">Professional service</span></div>
    <div class="acc-body">When you hire a Tavo Electrical Electrician you will get a professional and well-presented Electrician that comes skilled and ready to do the job.</div>
    <div class="acc-item"><span class="acc-sign">+</span><span class="acc-label">5 year workmanship guarantee</span></div>
    <div class="acc-item"><span class="acc-sign">+</span><span class="acc-label">Value for Money</span></div>
    <div class="acc-item"><span class="acc-sign">+</span><span class="acc-label">Environmentally friendly</span></div>
    <div class="acc-item"><span class="acc-sign">+</span><span class="acc-label">Fully insured</span></div>
  </div>
</section>

<section class="testimonials">
  <span class="quote-mark">“</span>
  <h2 class="section-title">TESTIMONIALS</h2>
  <svg class="avatar" viewBox="0 0 76 76">
    <circle cx="38" cy="38" r="38" fill="#c4202a"/>
    <circle cx="38" cy="29" r="13" fill="#fff"/>
    <path d="M14 64c4-14 14-20 24-20s20 6 24 20a38 38 0 0 1-48 0z" fill="#fff"/>
  </svg>
  <p class="user-name">User Name</p>
  <p class="quote-text">Lorem Ipsum is simply dummy text of the printing and typesetting industry. Lorem Ipsum has been the industry's standard dummy text ever since the 1500s, when an unknown printer took a galley of type and scrambled it to make a type specimen book.</p>
  <div class="quote-dots"><span class="on"></span><span></span><span></span></div>
</section>

<section class="contact">
  <h2 class="section-title">CONTACT US</h2>
  <div class="field field-name">Name</div>
  <div class="field field-email">Email</div>
  <div class="field field-message">Message</div>
  <span class="btn btn-primary">SUBMIT
    <svg viewBox="0 0 14 14"><path d="M1 7h11M8 3l4 4-4 4" stroke="#fff" stroke-width="2" fill="none"/></svg></span>
</section>

<footer class="site-footer">
  <div class="footer-brand">Tavo</div>
  <div class="call">
    <svg viewBox="0 0 32 32"><path d="M8 4l5 6-3 3c1 4 5 8 9 9l3-3 6 5-3 4C14 28 4 18 4 7z" fill="#fff"/></svg>
    <div><p class="footer-label">Call us now!</p><p class="call-number">123-555-0147</p></div>
  </div>
  <div class="follow">
    <p class="footer-label">Follow us!</p>
    <div class="social" aria-label="Social links"><span></span><span></span><span></span></div>
  </div>
  <div class="subscribe">
    <p class="footer-label">Subscribe!</p>
    <div class="sub-input">Enter Email</div>
  </div>
</footer>
<div class="copyright">All Copyrights Reserved by Tavo Electrical</div>
<div class="to-top"><svg width="20" height="20" viewBox="0 0 20 20"><path d="M3 13l7-7 7 7" stroke="#fff" stroke-width="2.5" fill="none"/></svg></div>

</body>
</html>
```